Business Card and Letterhead Design

Need to design business cards. I have attached logo. Information should both be front and back. The logo ([url removed, login to view]) and the psd file for logo ([url removed, login to view]) are both attached. Here is further details for the card:

Name: Mirela Okonsky
Title: Life Coach
Phone Number: 503-218-9361
Email: mirela@[url removed, login to view]
Slogan: Inspire, Transform, Happiness

```html
<!DOCTYPE html>
<html lang="en">
<head>
<meta charset="utf-8">
<title>Navira Business Card</title>
<link href="https://fonts.googleapis.com/css2?family=Josefin+Sans:wght@400;600&display=swap" rel="stylesheet">
<style>
  :root {
    --stage: #cfcfcf;
    --stage-light: #e4e4e4;
    --card-black: #0b0b0b;
    --card-grey: #3a3c3b;
    --card-grey-dark: #232524;
    --silver: #d9d9d9;
    --ink: #111111;
    --green: #1f7a35;
    --white: #f2f2f2;
    --muted: #bdbdbd;
  }
  * { margin: 0; padding: 0; box-sizing: border-box; }
  html, body { width: 1200px; height: 543px; overflow: hidden; }
  body {
    background: radial-gradient(ellipse at 50% 45%, var(--stage-light), var(--stage));
    font-family: "Josefin Sans", sans-serif;
    position: relative;
  }
  .card {
    position: absolute;
    top: 128px;
    width: 500px;
    height: 286px;
    overflow: hidden;
    box-shadow: 0 10px 24px rgba(0,0,0,0.35);
  }
  .card svg.swoosh { position: absolute; inset: 0; }
  .card--front { left: 70px; background: linear-gradient(160deg, var(--card-grey), var(--card-grey-dark)); }
  .card--back { left: 630px; background: var(--card-black); }

  .brand {
    position: absolute; left: 0; right: 0; top: 104px;
    display: flex; align-items: center; justify-content: center; gap: 10px;
  }
  .brand__name { font-size: 40px; font-weight: 600; letter-spacing: 2px; color: var(--ink); }
  .brand__dot { width: 22px; height: 22px; border-radius: 50%; background: var(--green); }
  .brand__tagline {
    position: absolute; left: 0; right: 0; top: 152px; text-align: center;
    font-size: 10px; letter-spacing: 1.5px; color: var(--green);
  }
  .slogan {
    position: absolute; left: 0; right: 0; bottom: 30px; text-align: center;
    font-size: 14px; letter-spacing: 1px; color: var(--green);
  }

  .person { position: absolute; left: 40px; top: 34px; color: var(--white); }
  .person__name { font-size: 24px; font-weight: 400; letter-spacing: 1px; text-transform: uppercase; }
  .person__title {
    margin-top: 6px; margin-left: 110px; font-size: 11px; font-variant: small-caps;
    letter-spacing: 1px; color: var(--muted);
  }
  .contact { position: absolute; left: 42px; top: 120px; list-style: none; }
  .contact li {
    display: flex; align-items: center; gap: 12px;
    font-size: 9px; color: var(--muted); margin-bottom: 12px;
  }
  .contact svg { width: 11px; height: 11px; fill: var(--white); }
  .faint-brand {
    position: absolute; right: 70px; bottom: 40px;
    font-size: 30px; font-weight: 600; letter-spacing: 2px; color: rgba(31,122,53,0.18);
  }
</style>
</head>
<body>

<section class="card card--front" aria-label="Card front">
  <svg class="swoosh" viewBox="0 0 500 286" aria-hidden="true">
    <defs>
      <linearGradient id="bandDark" x1="0" y1="0" x2="1" y2="0">
        <stop offset="0" stop-color="#151515"/>
        <stop offset="1" stop-color="#2c2d2c"/>
      </linearGradient>
    </defs>
    <path d="M0 0 H70 Q20 143 70 286 H0 Z" fill="url(#bandDark)"/>
    <path d="M70 0 Q20 143 70 286" fill="none" stroke="var(--silver)" stroke-width="1.5" opacity="0.8"/>
    <path d="M45 0 Q5 143 45 286" fill="none" stroke="var(--silver)" stroke-width="0.8" opacity="0.5"/>
    <path d="M500 0 H430 Q480 143 430 286 H500 Z" fill="url(#bandDark)"/>
    <path d="M430 0 Q480 143 430 286" fill="none" stroke="var(--silver)" stroke-width="1.5" opacity="0.8"/>
    <path d="M455 0 Q495 143 455 286" fill="none" stroke="var(--silver)" stroke-width="0.8" opacity="0.5"/>
  </svg>
  <div class="brand">
    <span class="brand__name">NAVIRA</span>
    <span class="brand__dot"></span>
  </div>
  <p class="brand__tagline">Coaching for a Brighter Life</p>
  <p class="slogan">Inspire, Transform, Happiness</p>
</section>

<section class="card card--back" aria-label="Card back">
  <svg class="swoosh" viewBox="0 0 500 286" aria-hidden="true">
    <path d="M330 0 H500 V286 H250 Q400 150 330 0 Z" fill="#1d1e1e"/>
    <path d="M330 0 Q400 150 250 286" fill="none" stroke="var(--silver)" stroke-width="1.6" opacity="0.85"/>
    <path d="M400 0 Q470 150 330 286" fill="none" stroke="var(--silver)" stroke-width="1.2" opacity="0.7"/>
  </svg>
  <div class="person">
    <h1 class="person__name">Mirela Okonsky</h1>
    <p class="person__title">Life Coach</p>
  </div>
  <ul class="contact">
    <li>
      <svg viewBox="0 0 24 24"><path d="M6.6 10.8a15 15 0 0 0 6.6 6.6l2.2-2.2c.3-.3.7-.4 1-.2 1.1.4 2.3.6 3.6.6.6 0 1 .4 1 1V20c0 .6-.4 1-1 1A17 17 0 0 1 3 4c0-.6.4-1 1-1h3.5c.6 0 1 .4 1 1 0 1.3.2 2.5.6 3.6.1.3 0 .7-.2 1z"/></svg>
      <span>503-218-9361</span>
    </li>
    <li>
      <svg viewBox="0 0 24 24"><path d="M12 2a7 7 0 0 0-7 7c0 5 7 13 7 13s7-8 7-13a7 7 0 0 0-7-7zm0 9.5A2.5 2.5 0 1 1 12 6.5a2.5 2.5 0 0 1 0 5z"/></svg>
      <span>Address</span>
    </li>
    <li>
      <svg viewBox="0 0 24 24"><path d="M2 5h20v14H2z M2 5l10 8 10-8" fill="none" stroke="var(--white)" stroke-width="2"/></svg>
      <span>mirela@navira.com</span>
    </li>
  </ul>
  <span class="faint-brand">NAVIRA</span>
</section>

</body>
</html>
```